Wow me with your Earring card options!

An A7 portrait sized earring card is required for Marble & Mango. Inspired by Marble and fueled by Mango we love our accessories to do the talking. Bold statement earrings are our thing. Our earring cards need to showcase our brand while not stealing all of the limelight from the earrings themselves. Earring care information needs to be included on the back side of the card. Our simple logo needs to be the basis for the colour choices used on the card.

Requirements
Should not have
• No florals please 😊

```html
<!DOCTYPE html>
<html lang="en">
<head>
<meta charset="utf-8">
<title>Marble &amp; Mango — Earring Cards</title>
<link rel="stylesheet" href="https://fonts.googleapis.com/css2?family=Lora:wght@400;500;600&display=swap">
<style>
  :root {
    --backdrop: #fdf7dc;
    --card: #000000;
    --ink: #f2f2f2;
    --ink-soft: #cfcfcf;
    --brush: #3a3a3a;
    --chip: #2a2a2a;
    --bloom-violet: #5b1ee0;
    --bloom-coral: #ef5a5a;
    --bloom-lime: #a6d95a;
    --font-text: "Lora", Georgia, serif;
  }
  * { box-sizing: border-box; margin: 0; padding: 0; }
  html, body { width: 1200px; height: 1200px; overflow: hidden; }
  body { background: var(--backdrop); position: relative; font-family: var(--font-text); color: var(--ink); }

  .card {
    position: absolute;
    width: 533px;
    height: 748px;
    background: var(--card);
    box-shadow: 0 2px 6px rgba(0,0,0,0.35);
    overflow: hidden;
  }
  .card--back { left: 54px; top: 54px; }
  .card--front { left: 625px; top: 396px; }

  .wordmark {
    position: absolute;
    font-family: var(--font-text);
    font-weight: 600;
    color: var(--ink);
    text-align: center;
    line-height: 1.05;
    letter-spacing: 1px;
  }
  .card--back .wordmark { left: 100px; width: 350px; top: 130px; font-size: 50px; }
  .card--front .wordmark { left: 40px; width: 450px; top: 280px; font-size: 66px; }

  .bloom { position: absolute; }
  .bloom--top-left { left: 0; top: 10px; width: 220px; height: 245px; }
  .bloom--bottom-right { right: 0; bottom: 0; width: 215px; height: 240px; }

  .care-list { position: absolute; left: 42px; top: 305px; list-style: none; }
  .care-item { display: flex; align-items: center; height: 52px; }
  .care-icon { position: relative; width: 58px; height: 44px; margin-right: 17px; }
  .care-icon .brush { position: absolute; left: 2px; top: 10px; width: 54px; height: 26px; border-radius: 14px 6px 16px 8px; background: var(--brush); transform: rotate(-6deg); }
  .care-icon svg { position: absolute; left: 11px; top: 4px; width: 36px; height: 36px; }
  .care-text { font-size: 18.5px; font-weight: 400; letter-spacing: 0.3px; white-space: nowrap; }

  .contact { position: absolute; list-style: none; }
  .card--back .contact { left: 48px; top: 617px; }
  .card--front .contact { left: 44px; top: 603px; }
  .contact-line { display: flex; align-items: center; height: 21.5px; font-size: 10px; color: var(--ink); }
  .contact-line svg { width: 14px; height: 14px; margin-right: 17px; }

  .social { position: absolute; display: flex; gap: 8px; }
  .card--back .social { left: 50px; top: 694px; }
  .card--front .social { left: 46px; top: 679px; }
  .social-item { display: flex; align-items: center; gap: 5px; font-size: 10px; color: var(--ink); }
  .social-item .chip { width: 14px; height: 14px; border-radius: 3px; background: var(--chip); border: 1px solid #555; }
</style>
</head>
<body>

<!-- Care side -->
<section class="card card--back">
  <svg class="bloom bloom--top-left" role="img" aria-label="Colourful botanical sprig illustration curving around the top-left corner" viewBox="0 0 220 245">
    <defs>
      <linearGradient id="bloomTL" x1="0" y1="1" x2="1" y2="0">
        <stop offset="0" stop-color="var(--bloom-lime)"/>
        <stop offset="0.45" stop-color="var(--bloom-violet)"/>
        <stop offset="1" stop-color="var(--bloom-coral)"/>
      </linearGradient>
    </defs>
    <path d="M10 245 C0 150 40 40 215 0 L220 30 C80 60 45 150 48 245 Z" fill="url(#bloomTL)" opacity="0.85"/>
  </svg>

  <div class="wordmark">Marble<br>&amp; Mango</div>

  <ul class="care-list">
    <li class="care-item">
      <span class="care-icon"><span class="brush"></span>
        <svg viewBox="0 0 36 36" fill="none" stroke="#fff" stroke-width="1.3"><path d="M14 10 C10 17 7 21 7 25 a7 7 0 0 0 14 0 c0-4-3-8-7-15z"/><path d="M25 4 c-2 4-4 6-4 8 a4 4 0 0 0 8 0 c0-2-2-4-4-8z"/></svg>
      </span>
      <span class="care-text">Avoid moisture &amp; remove before bathing</span>
    </li>
    <li class="care-item">
      <span class="care-icon"><span class="brush"></span>
        <svg viewBox="0 0 36 36" fill="none" stroke="#fff" stroke-width="1.3"><rect x="6" y="9" width="24" height="10" rx="3"/><rect x="9" y="12" width="8" height="5" rx="1.5"/><rect x="19" y="12" width="8" height="5" rx="1.5"/><rect x="4" y="19" width="28" height="6" rx="2"/><path d="M6 25v4M30 25v4"/></svg>
      </span>
      <span class="care-text">For comforts sake, remove before bed!</span>
    </li>
    <li class="care-item">
      <span class="care-icon"><span class="brush"></span>
        <svg viewBox="0 0 36 36" fill="none" stroke="#fff" stroke-width="1.3"><circle cx="16" cy="23" r="9"/><rect x="13" y="10" width="6" height="4"/><path d="M16 10V5h6M22 5a3 2 0 1 0 6 0a3 2 0 1 0-6 0"/><path d="M9 32h14"/></svg>
      </span>
      <span class="care-text">Avoid contact with perfume &amp; lotions</span>
    </li>
    <li class="care-item">
      <span class="care-icon"><span class="brush"></span>
        <svg viewBox="0 0 36 36" fill="none" stroke="#fff" stroke-width="1.3"><circle cx="18" cy="18" r="7"/><path d="M18 3v6M18 27v6M3 18h6M27 18h6M7.5 7.5l4 4M24.5 24.5l4 4M28.5 7.5l-4 4M11.5 24.5l-4 4"/></svg>
      </span>
      <span class="care-text">Store away from direct sunlight</span>
    </li>
  </ul>

  <ul class="contact">
    <li class="contact-line"><svg viewBox="0 0 14 14" fill="none" stroke="#fff" stroke-width="0.8"><circle cx="7" cy="7" r="6"/><ellipse cx="7" cy="7" rx="2.6" ry="6"/><path d="M1 7h12M2 4h10M2 10h10"/></svg>www.marbleandmango.com.au</li>
    <li class="contact-line"><svg viewBox="0 0 14 14" fill="none" stroke="#fff" stroke-width="0.8"><rect x="1" y="3" width="12" height="9"/><path d="M1 3l6 5 6-5"/></svg>hello@marbleandmango.com.au</li>
    <li class="contact-line"><svg viewBox="0 0 14 14" fill="none" stroke="#fff" stroke-width="0.8"><circle cx="7" cy="7" r="6"/><circle cx="7" cy="5.5" r="2.2"/><path d="M3 11.5c1-2 7-2 8 0"/></svg>@marbleandmango</li>
  </ul>

  <div class="social">
    <span class="social-item"><span class="chip"></span>Tokko</span>
    <span class="social-item"><span class="chip"></span>Pinly</span>
    <span class="social-item"><span class="chip"></span>Facely</span>
    <span class="social-item"><span class="chip"></span>Snapgram</span>
  </div>

  <svg class="bloom bloom--bottom-right" role="img" aria-label="Colourful botanical sprig illustration curving around the bottom-right corner" viewBox="0 0 215 240">
    <defs>
      <linearGradient id="bloomBR" x1="1" y1="0" x2="0" y2="1">
        <stop offset="0" stop-color="var(--bloom-lime)"/>
        <stop offset="0.5" stop-color="var(--bloom-violet)"/>
        <stop offset="1" stop-color="var(--bloom-coral)"/>
      </linearGradient>
    </defs>
    <path d="M205 0 C215 100 175 200 0 225 L5 240 C150 240 215 180 215 0 Z" fill="url(#bloomBR)" opacity="0.85"/>
  </svg>
</section>

<!-- Display side -->
<section class="card card--front">
  <div class="wordmark">Marble<br>&amp; Mango</div>

  <ul class="contact">
    <li class="contact-line"><svg viewBox="0 0 14 14" fill="none" stroke="#fff" stroke-width="0.8"><circle cx="7" cy="7" r="6"/><ellipse cx="7" cy="7" rx="2.6" ry="6"/><path d="M1 7h12M2 4h10M2 10h10"/></svg>www.marbleandmango.com.au</li>
    <li class="contact-line"><svg viewBox="0 0 14 14" fill="none" stroke="#fff" stroke-width="0.8"><rect x="1" y="3" width="12" height="9"/><path d="M1 3l6 5 6-5"/></svg>hello@marbleandmango.com.au</li>
    <li class="contact-line"><svg viewBox="0 0 14 14" fill="none" stroke="#fff" stroke-width="0.8"><circle cx="7" cy="7" r="6"/><circle cx="7" cy="5.5" r="2.2"/><path d="M3 11.5c1-2 7-2 8 0"/></svg>@marbleandmango</li>
  </ul>

  <div class="social">
    <span class="social-item"><span class="chip"></span>Tokko</span>
    <span class="social-item"><span class="chip"></span>Pinly</span>
    <span class="social-item"><span class="chip"></span>Facely</span>
    <span class="social-item"><span class="chip"></span>Snapgram</span>
  </div>
</section>

</body>
</html>
```